IT Company based on Biology Business Needs a Business Card Design

We need a business card design for a new company called 'Lumen CELL'. We develop the machine learning solutions especially focused on deep learning algorithms for biology industry. Our initial product is a vision detection on biological images to help doctors diagnose the symptoms. We would like to see designs that use the color green.

Industry/Entity Type

Business

```html
<!DOCTYPE html>
<html lang="en">
<head>
<meta charset="utf-8">
<title>Lumen CELL – Business Card</title>
<link rel="stylesheet" href="https://fonts.googleapis.com/css2?family=Arimo:wght@400;700&display=swap">
<style>
  :root {
    --backdrop: #d9d9d6;
    --card-black: #141414;
    --card-edge: #0a0a0a;
    --green: #6cc83a;
    --green-deep: #2fa046;
    --text-light: #f2f2f2;
    --gloss-grey: #6b6b6b;
    --divider: #8a8a8a;
  }
  * { box-sizing: border-box; margin: 0; padding: 0; }
  html, body { width: 1200px; height: 787px; overflow: hidden; }
  body {
    background: var(--backdrop);
    font-family: "Arimo", Arial, sans-serif;
    display: flex;
    align-items: center;
    justify-content: center;
    gap: 40px;
  }
  .card {
    width: 540px;
    height: 309px;
    background: var(--card-black);
    border: 1px solid var(--card-edge);
    box-shadow: 0 6px 18px rgba(0,0,0,0.25);
    position: relative;
  }
  .card-back {
    display: flex;
    align-items: center;
    justify-content: center;
  }
  .brand {
    display: flex;
    align-items: center;
    gap: 14px;
    font-weight: 700;
    letter-spacing: -0.5px;
  }
  .brand-dot { border-radius: 50%; flex: none; }
  .card-back .brand { font-size: 50px; color: var(--gloss-grey); }
  .card-back .brand-dot { width: 34px; height: 34px; background: var(--gloss-grey); }
  .card-front .brand {
    position: absolute;
    top: 64px;
    left: 150px;
    font-size: 48px;
    color: var(--green);
  }
  .card-front .brand-dot { width: 32px; height: 32px; background: var(--green); }
  .contact-block {
    position: absolute;
    left: 40px;
    right: 30px;
    top: 180px;
    display: flex;
    align-items: stretch;
    gap: 18px;
  }
  .identity {
    flex: 1;
    text-align: right;
    color: var(--text-light);
    font-size: 14px;
    line-height: 1.35;
  }
  .person-name { color: var(--green); font-weight: 700; font-size: 17px; }
  .person-role { color: var(--green-deep); font-size: 14px; margin-bottom: 2px; }
  .divider { width: 1px; background: var(--divider); }
  .details {
    flex: 1;
    list-style: none;
    color: var(--text-light);
    font-size: 14.5px;
    line-height: 1.55;
    padding-top: 6px;
  }
  .details li { display: flex; align-items: center; gap: 8px; }
  .details svg { width: 14px; height: 14px; fill: var(--green); flex: none; }
</style>
</head>
<body>
  <section class="card card-back" aria-label="Card back">
    <div class="brand"><span class="brand-dot"></span><span class="brand-name">LUMEN CELL</span></div>
  </section>

  <section class="card card-front" aria-label="Card front">
    <div class="brand"><span class="brand-dot"></span><span class="brand-name">LUMEN CELL</span></div>

    <div class="contact-block">
      <div class="identity">
        <p class="person-name">Marin Hale</p>
        <p class="person-role">President</p>
        <p class="address">2417 Harbor Lane<br>Glen Ridge, NY 10980</p>
      </div>
      <div class="divider"></div>
      <ul class="details">
        <li>
          <svg viewBox="0 0 16 16" aria-hidden="true"><path d="M3 1h3l1 4-2 1.5a9 9 0 0 0 4.5 4.5L11 9l4 1v3a2 2 0 0 1-2 2A12 12 0 0 1 1 3a2 2 0 0 1 2-2z"/></svg>
          <span>555 0142 7781</span>
        </li>
        <li>
          <svg viewBox="0 0 16 16" aria-hidden="true"><path d="M4 0h8a1 1 0 0 1 1 1v14a1 1 0 0 1-1 1H4a1 1 0 0 1-1-1V1a1 1 0 0 1 1-1zm1 2v10h6V2zm3 11a1 1 0 1 0 0 2 1 1 0 0 0 0-2z"/></svg>
          <span>555 0199 3046</span>
        </li>
        <li>
          <svg viewBox="0 0 16 16" aria-hidden="true"><path d="M0 3h16v10H0zm1.5 1.2V12h13V4.2L8 9z"/></svg>
          <span>marin@example.com</span>
        </li>
        <li>
          <svg viewBox="0 0 16 16" aria-hidden="true"><circle cx="8" cy="8" r="7.5"/></svg>
          <span>www.example.com</span>
        </li>
      </ul>
    </div>
  </section>
</body>
</html>
```